Web design for financial services

A modern web design of financial services (brokerage firm)
Req.s and technology tags :
- Very mobile friendly.
- One paged with some inner pages.
- Animated sticky header .
- Member login area for e-trade.
- Support RTL language.
- HTML & CSS.

The logo will be Home link
• ORNY :
WHO WE ARE
Content :
i) Board of Directors
ii) Mission Statement
iii) Corporate Values
iv) Regulations
• Financial Services :
WHAT WE DO
Content:
i) Electronic trading
ii) Trading desk
iii) Institutional
iv) Investors Education
• News
• Market Tools
• Forms---- opens new page
• Careers---- opens new page
• Contact Us----opens new page

The website is :
http://www.orny-halvet.com/

The logo need some changes to be more modern and impressively , but with keeping same structure .

Some related websites :
https://www.vexdalo.com.qa/

financial market

Financial Service

2 page

• same fonts of http://www.tuwmallow.com/

• - Very mobile friendly.
• - One paged with some inner pages.
• - Animated sticky header .
• - Member login area for e-trade.
• - Support RTL language.
• - HTML & CSS.
• Slider , some Qatari theme,
• i like the video inside the home page
• ex :http://www.tuwmallow.com/

```html
<!DOCTYPE html>
<html lang="en">
<head>
<meta charset="utf-8">
<title>ORNY — Forms</title>
<link rel="stylesheet" href="https://fonts.googleapis.com/css2?family=Open+Sans:ital,wght@0,400;0,600;0,700;1,400&display=swap">
<style>
  :root {
    --brand-red: #9b2423;
    --ink: #1d1d1d;
    --text: #333333;
    --muted: #777777;
    --field-bg: #e8e8e8;
    --field-border: #d6d6d6;
    --rule: #dddddd;
    --footer-bg: #000000;
    --white: #ffffff;
  }
  * { box-sizing: border-box; margin: 0; padding: 0; }
  html, body { width: 1200px; height: 2493px; overflow: hidden; }
  body {
    position: relative;
    background: var(--white);
    font-family: "Open Sans", Arial, sans-serif;
    color: var(--text);
  }

  /* Header */
  .site-header { position: absolute; left: 0; top: 0; width: 1200px; height: 120px; background: var(--white); }
  .brand { position: absolute; left: 78px; top: 40px; display: flex; align-items: center; gap: 12px; text-decoration: none; }
  .brand-mark { width: 34px; height: 34px; background: var(--brand-red); }
  .brand-name { font-size: 44px; font-weight: 700; color: var(--ink); letter-spacing: -1px; line-height: 1; }
  .header-tools { position: absolute; right: 76px; top: 26px; display: flex; gap: 10px; }
  .btn-etrade {
    height: 27px; padding: 0 12px; background: var(--brand-red); color: var(--white);
    font-size: 10px; font-weight: 700; display: flex; align-items: center; gap: 6px; border-radius: 2px;
  }
  .btn-etrade .icon { width: 10px; height: 10px; border: 1.5px solid var(--white); }
  .lang-select {
    height: 27px; padding: 0 10px; border: 1px solid #999; border-radius: 2px; color: var(--ink);
    font-size: 9px; font-weight: 600; display: flex; align-items: center; gap: 6px;
  }
  .lang-select .flag { width: 14px; height: 9px; background: #c8cfe0; }
  .main-nav { position: absolute; right: 75px; top: 81px; display: flex; gap: 35px; }
  .main-nav a { font-size: 12.5px; font-weight: 700; color: var(--ink); text-decoration: none; }
  .main-nav a.is-active { color: var(--brand-red); }

  /* Hero */
  .hero { position: absolute; left: 0; top: 120px; width: 1200px; height: 545px; overflow: hidden; }
  .hero-photo {
    position: absolute; inset: 0;
    background: linear-gradient(120deg, #2b2c30 0%, #4a3a2c 35%, #6b5a48 55%, #3d3f45 80%, #25262a 100%);
  }
  .hero-title {
    position: absolute; left: 0; top: 175px; width: 1200px; text-align: center;
    color: var(--white); font-size: 64px; font-weight: 700; letter-spacing: 1px;
  }
  .hero-cut { position: absolute; left: 0; top: 0; }

  /* Content */
  .side-nav { position: absolute; left: 160px; top: 700px; }
  .side-nav-title { font-size: 15px; font-weight: 700; color: var(--brand-red); }
  .side-nav-bar { width: 46px; height: 4px; background: var(--ink); margin-top: 12px; }
  .side-nav-link { display: block; margin-top: 19px; font-size: 11px; font-weight: 700; color: var(--ink); text-decoration: none; }
  .column-rule { position: absolute; left: 339px; top: 698px; width: 1px; height: 1094px; background: var(--rule); }

  .article { position: absolute; left: 381px; top: 697px; width: 658px; }
  .article h1 { font-size: 21px; font-weight: 700; color: var(--brand-red); }
  .article .lead { margin-top: 14px; font-size: 13.5px; font-style: italic; color: var(--ink); }
  .article p.body { margin-top: 17px; font-size: 10.6px; line-height: 20px; color: var(--text); }
  .article p.body + p.body { margin-top: 22px; }
  .article p.body.spaced { margin-top: 32px; }

  .complaint-form { position: absolute; left: 381px; top: 1168px; width: 658px; }
  .form-head { display: flex; justify-content: space-between; align-items: baseline; padding-bottom: 14px; border-bottom: 1px solid var(--rule); }
  .form-head h2 { font-size: 21px; font-weight: 700; color: var(--brand-red); }
  .form-head .note { font-size: 10.5px; font-style: italic; color: var(--muted); }
  .field-grid { display: grid; grid-template-columns: 320px 321px; column-gap: 17px; margin-top: 20px; }
  .field { margin-bottom: 20px; }
  .field label { display: block; font-size: 11px; color: var(--ink); height: 17px; }
  .field label .req { color: var(--brand-red); }
  .field .input {
    height: 37px; background: var(--field-bg); border: 1px solid var(--field-border);
    display: flex; align-items: center; justify-content: space-between; padding: 0 10px;
    font-size: 11px; color: var(--ink);
  }
  .field .caret { width: 0; height: 0; border-left: 6px solid transparent; border-right: 6px solid transparent; border-top: 6px solid var(--ink); }
  .field.wide { grid-column: 1 / span 2; margin-top: 10px; }
  .field .textarea { height: 148px; background: var(--field-bg); border: 1px solid var(--field-border); }
  .btn-submit {
    width: 113px; height: 37px; background: var(--brand-red); color: var(--white);
    font-size: 13px; font-weight: 700; display: flex; align-items: center; justify-content: center;
    margin-top: -3px; border-radius: 2px;
  }

  /* Skyline band */
  .skyline {
    position: absolute; left: 0; top: 1911px; width: 1200px; height: 328px;
    background: linear-gradient(180deg, #ffffff 0%, #ecd3d2 30%, #c98b89 65%, #8e3836 100%);
  }

  /* Footer */
  .site-footer { position: absolute; left: 0; top: 2239px; width: 1200px; height: 254px; background: var(--footer-bg); color: var(--white); text-align: center; }
  .footer-brand { position: absolute; left: 0; top: 50px; width: 1200px; display: flex; justify-content: center; align-items: center; gap: 10px; }
  .footer-brand .brand-mark { width: 26px; height: 26px; border: 3px solid var(--white); background: transparent; }
  .footer-brand .brand-name { color: var(--white); font-size: 32px; }
  .footer-nav { position: absolute; left: 0; top: 127px; width: 1200px; display: flex; justify-content: center; gap: 18px; font-size: 13px; font-weight: 700; }
  .footer-nav a { color: var(--white); text-decoration: none; }
  .footer-nav .sep { color: var(--white); }
  .footer-legal { position: absolute; left: 0; top: 160px; width: 1200px; font-size: 10px; color: #dddddd; }
  .social-list { position: absolute; left: 520px; top: 192px; display: flex; gap: 10px; }
  .social-list span { width: 24px; height: 24px; border: 1.5px solid var(--white); border-radius: 50%; }
</style>
</head>
<body>

<header class="site-header">
  <a class="brand" href="#"><span class="brand-mark"></span><span class="brand-name">ORNY</span></a>
  <div class="header-tools">
    <div class="btn-etrade"><span class="icon"></span>ORNY E-TRADE</div>
    <div class="lang-select"><span class="flag"></span>ENGLISH
      <svg width="8" height="6" viewBox="0 0 8 6"><path d="M1 1l3 3 3-3" fill="none" stroke="#1d1d1d" stroke-width="1.3"/></svg>
    </div>
  </div>
  <nav class="main-nav">
    <a href="#">ORNY</a>
    <a href="#">FINANCIAL SERVICE</a>
    <a href="#">NEWS</a>
    <a href="#">MARKET TOOL</a>
    <a href="#" class="is-active">FORMS</a>
    <a href="#">CAREERS</a>
    <a href="#">CONTACT US</a>
  </nav>
</header>

<section class="hero">
  <div class="hero-photo" role="img" aria-label="Photo of hands reviewing financial charts beside a laptop on a desk"></div>
  <h1 class="hero-title">FORMS</h1>
  <svg class="hero-cut" width="1200" height="545" viewBox="0 0 1200 545">
    <polygon points="0,470 374,400 1200,545 0,545" fill="#ffffff"/>
  </svg>
</section>

<aside class="side-nav">
  <div class="side-nav-title">FORMS</div>
  <div class="side-nav-bar"></div>
  <a class="side-nav-link" href="#">COMPLAINTS</a>
</aside>
<div class="column-rule"></div>

<article class="article">
  <h1>Filling a Complaint</h1>
  <p class="lead">What should I do if I have a complaint?</p>
  <p class="body">We take every concern from our clients seriously and aim to resolve it in a fair, prompt and open manner. If you feel that a service, a trade or a statement did not meet your expectations, please tell us as soon as possible so that our team can review the matter, check the records and contact you with a clear answer within the stated time.</p>
  <p class="body spaced">Before you submit a complaint, please gather the details of the order, the account number, the date and time of the ticket and any messages you have received from us. Complete information helps our officers trace the issue quickly and give you an accurate reply without delay in most cases.</p>
  <p class="body spaced">Once your complaint is received, it will be logged and assigned to a member of the compliance team who is not involved in the original matter. You will receive an acknowledgement by email with a reference number that you can quote in any later contact. We will study the facts, review the recorded calls and the trading system logs, and may ask you for further documents where needed. Our goal is to send a final written response within fifteen working days. If the case is complex and needs more time, we will write to explain the reason and give a new expected date. If you are not satisfied with our final answer, you may refer the matter to the relevant market regulator for an independent review.</p>
</article>

<section class="complaint-form">
  <div class="form-head">
    <h2>Client Complaints Form</h2>
    <span class="note">* mandatory fields</span>
  </div>
  <div class="field-grid">
    <div class="field"><label>Complaint Type <span class="req">*</span></label><div class="input">Choose one<span class="caret"></span></div></div>
    <div class="field"><label>Email Address <span class="req">*</span></label><div class="input"></div></div>
    <div class="field"><label>Phone <span class="req">*</span></label><div class="input"></div></div>
    <div class="field"><label>Subject <span class="req">*</span></label><div class="input"></div></div>
    <div class="field"><label>Account Name <span class="req">*</span></label><div class="input"></div></div>
    <div class="field"><label>Account Number <span class="req">*</span></label><div class="input"></div></div>
    <div class="field"><label>Order/Ticket Number <span class="req">*</span></label><div class="input"></div></div>
    <div class="field"><label>Date and time of the order/ticket <span class="req">*</span></label><div class="input"></div></div>
    <div class="field wide"><label>Description of complaint <span class="req">*</span></label><div class="textarea"></div></div>
  </div>
  <div class="btn-submit">SUBMIT</div>
</section>

<div class="skyline" role="img" aria-label="Illustration of the Doha city skyline in red tones"></div>

<footer class="site-footer">
  <div class="footer-brand"><span class="brand-mark"></span><span class="brand-name">ORNY</span></div>
  <nav class="footer-nav">
    <a href="#">ORNY</a><span class="sep">|</span>
    <a href="#">FIANCIAL SERVICE</a><span class="sep">|</span>
    <a href="#">NEWS</a><span class="sep">|</span>
    <a href="#">MARKET TOOL</a><span class="sep">|</span>
    <a href="#">CAREERS</a><span class="sep">|</span>
    <a href="#">CONTACT US</a>
  </nav>
  <div class="footer-legal">©2017. All Rights Reserved | ORNY Qatar | Copyright, Legal and Privacy Statement.Disclaimers and Legal Information</div>
  <div class="social-list"><span></span><span></span><span></span><span></span><span></span></div>
</footer>

</body>
</html>
```